Business Card Design - cloud video monitoring

For the trade show in Las Vegas our company needs business cards with new brand - Vyrolux

The logo of the new brand is attached, the sample card with the founder's contact details is attached (just change the website to www.vyrolux.me) and email to info@vyrolux.me
Updates

                                        Forgot to say: the tagline for the brand is "the new normal cloud video management"

Industry/Entity Type

Business

```html
<!DOCTYPE html>
<html lang="en">
<head>
<meta charset="utf-8">
<title>Vyrolux — Business Card</title>
<link rel="stylesheet" href="https://fonts.googleapis.com/css2?family=Open+Sans:wght@400;600;700&display=swap">
<style>
  :root {
    --backdrop: #e6e4e0;
    --card: #323335;
    --card-edge: #2a2b2d;
    --glow: rgba(255, 255, 255, 0.07);
    --glow-soft: rgba(255, 255, 255, 0.045);
    --teal: #4fc4a9;
    --ink: #f4f4f4;
  }
  html, body {
    margin: 0;
    padding: 0;
    width: 1200px;
    height: 1014px;
    overflow: hidden;
    background: var(--backdrop);
    font-family: "Open Sans", Arial, sans-serif;
  }
  .business-card {
    position: absolute;
    left: 150px;
    top: 250px;
    width: 900px;
    height: 514px;
    background: linear-gradient(135deg, #3a3b3d 0%, var(--card) 55%, var(--card-edge) 100%);
    border-radius: 6px;
    overflow: hidden;
    box-shadow: 0 18px 40px rgba(0, 0, 0, 0.25);
  }
  .card-shapes {
    position: absolute;
    inset: 0;
  }
  .brand {
    position: absolute;
    left: 520px;
    top: 118px;
    color: var(--teal);
  }
  .brand-line {
    display: flex;
    align-items: center;
    gap: 22px;
  }
  .brand-dot {
    width: 86px;
    height: 86px;
    border-radius: 50%;
    background: var(--teal);
  }
  .brand-name {
    font-size: 52px;
    font-weight: 400;
    letter-spacing: 0.5px;
    line-height: 1;
  }
  .tagline {
    margin: 26px 0 0 100px;
    font-size: 22px;
    line-height: 1.15;
    font-weight: 400;
  }
  .contact {
    position: absolute;
    left: 70px;
    top: 270px;
    color: var(--ink);
  }
  .person-name {
    font-size: 25px;
    font-weight: 700;
    margin: 0;
    line-height: 1.2;
  }
  .person-role {
    font-size: 22px;
    color: var(--teal);
    margin: 0 0 28px;
    line-height: 1.2;
  }
  .contact-list {
    list-style: none;
    margin: 0;
    padding: 0;
    font-size: 21px;
    line-height: 1.3;
  }
  .label, .accent {
    color: var(--teal);
  }
</style>
</head>
<body>
  <article class="business-card">
    <svg class="card-shapes" width="900" height="514" viewBox="0 0 900 514" aria-hidden="true">
      <circle cx="250" cy="620" r="470" fill="var(--glow-soft)"/>
      <circle cx="660" cy="200" r="215" fill="var(--glow)"/>
    </svg>

    <div class="brand">
      <div class="brand-line">
        <span class="brand-dot"></span>
        <span class="brand-name">Vyrolux</span>
      </div>
      <p class="tagline">the new normal<br>cloud video management</p>
    </div>

    <div class="contact">
      <h1 class="person-name">Mara Delvenko</h1>
      <p class="person-role">Founder</p>
      <ul class="contact-list">
        <li><span class="label">tel.:</span> +1.555.201.4470</li>
        <li><span class="label">fax.:</span> +1.555.318.2064</li>
        <li>info@vyrolux.me</li>
        <li>www.<span class="accent">vyrolux</span>.me</li>
      </ul>
    </div>
  </article>
</body>
</html>
```